New Stationary Design

Harlow Voltworks Ltd have acquired Brackmoor Kitchen Supply Ltd. We will be retaining the Brackmoor Kitchen Supply Ltd name and require new letter head, compliment slips & business card designs.

I have attached the existing Harlow Voltworks letterhead to show our current image/brand. I do not wish to change this substantially & imagine maybe a swap of colours from Red logo to Blue, and the title & footer bars maybe in Red. That said, I'm open to subtle changes in the overall design & to maybe modernise it and if we like them, we would probably ask the Designer to update the changes to reflect them on the Harlow Voltworks stationary as well.

We will be able to get some proper high def images for Catering equipment to include, but for the time being if desingers can use any standard stock images for initial presentation.

The logo will be printed onto a Red van so somehow we need to be able to modify it for that use.

Brackmoor Kitchen Supply Ltd. Correspondence Address: 47 Lower Fenwick Road, Northampton. NN3 8QX. Tel 01604 738 092. Fax 01604 738 416. No website currently. Registered No: 05817264. Vat No: 418 3052 96. Company Registered Address: 22 Calloway Close, Leicester. LE2 7RN. We would also like to mention that we have Regional Service Centres also based in Leicester & Stockport.

Business Cards would be for;

Owen Pritchard, Director. owen.pritchard@brackmoorkitchensupply.co.uk

Trevor Holbrook, Operations Manager. trevor.holbrook@brackmoorkitchensupply.co.uk

Neil Dunmore, Service Manager. neil.dunmore@brackmoorkitchensupply.co.uk

Simon Ketley, Business Development Manager. simon.ketley@brackmoorkitchensupply.co.uk

We would also like the letter head to include the 'Flue Sure' logo & our registration Number: To be confirmed. Also the Electrical Contractors logo & the words Wiring Trades Guild underneath so people know what it means. See www.wtgx.co.uk

Target Market(s)

Businesses who use Catering Equipment such as Cookers. fridges etc. Hence, Care Homes, Hospitals, Restaurants etc

Industry/Entity Type

Business

Requirements
Must have
• Resemblance to existing Harlow Voltworks brand, although maybe with some changes & modernisation.
Nice to have
• Could maybe have some 'icons' for the type of equipment we sell instead of photos. Ie Cookers, Ovens, Fridges, Microwaves, Dishwashers, as well as kithen cateringtabling, commercial extraction hoods etc.

```html
<!DOCTYPE html>
<html lang="en">
<head>
<meta charset="utf-8">
<title>Brackmoor Kitchen Supply – Compliment Slip</title>
<link rel="stylesheet" href="https://fonts.googleapis.com/css2?family=Carlito:wght@400;700&family=Marcellus&display=swap">
<style>
  :root {
    --brand-blue: #2b3990;
    --brand-red: #ed1c24;
    --paper: #ffffff;
    --backdrop: #ece9e4;
  }
  * { margin: 0; padding: 0; box-sizing: border-box; }
  html, body {
    width: 1200px;
    height: 1000px;
    overflow: hidden;
    background: var(--backdrop);
  }
  .canvas {
    position: relative;
    width: 1200px;
    height: 1000px;
  }
  .compliment-slip {
    position: absolute;
    left: 103px;
    top: 197px;
    width: 978px;
    height: 387px;
    background: var(--paper);
    box-shadow: 0 2px 6px rgba(0,0,0,0.12);
    font-family: "Carlito", "Calibri", sans-serif;
  }
  .brand {
    position: absolute;
    left: 18px;
    top: 18px;
  }
  .brand-name {
    color: var(--brand-blue);
    font-weight: 700;
    font-size: 30px;
    line-height: 1.02;
    letter-spacing: -0.3px;
  }
  .brand-affiliation {
    margin-top: 10px;
    color: var(--brand-blue);
    font-weight: 700;
    font-size: 12px;
  }
  .contact-block {
    position: absolute;
    left: 609px;
    top: 14px;
    padding-left: 9px;
    border-left: 2px solid var(--brand-red);
    font-size: 10.5px;
    line-height: 15.5px;
    color: var(--brand-blue);
  }
  .contact-block .label { color: var(--brand-red); }
  .contact-block .gap { margin-left: 10px; }
  .greeting {
    position: absolute;
    right: 34px;
    top: 334px;
    font-family: "Marcellus", "Georgia", serif;
    font-size: 34px;
    color: var(--brand-blue);
  }
  .footer-bar {
    position: absolute;
    left: 0;
    bottom: 0;
    width: 100%;
    height: 13px;
    background: var(--brand-red);
  }
</style>
</head>
<body>
<div class="canvas">
  <section class="compliment-slip">
    <div class="brand">
      <div class="brand-name">Brackmoor Kitchen<br>Supply</div>
      <div class="brand-affiliation">Wiring Trades Guild</div>
    </div>

    <div class="contact-block">
      <div><span class="label">Tel:</span> 01604 738 092 <span class="label gap">Fax:</span> 01604 738 416</div>
      <div><span class="label">Correspondence Address:</span> 47 Lower Fenwick Road, Northampton. NN3 8QX</div>
      <div><span class="label">Company Registered Address:</span> 22 Calloway Close, Leicester. LE2 7RN</div>
      <div>We have Regional Service Centres also based in Leicester &amp; Stockport.</div>
    </div>

    <p class="greeting">with best compliments...</p>

    <div class="footer-bar"></div>
  </section>
</div>
</body>
</html>
```